Business Card Design - Brightwater Dwellings

Hi there,

We would like a business card for our new venture, Brightwater Dwellings.

We are based in Western Australia and specialise in taking tired, old properties and making them look new again. We aim to create enjoyably liveable homes for young families in particular.

Product pricing is mid range i.e. appliances, furnishings, fixtures (not top end but not cheap either)

Our work is primarily cosmetic renovation (approx. 80%) and the rest construction (approx 20%).

We would like a business card that conveys the following:
- clean, simplistic/minimalistic design
- modern, contemporary style
- a touch of funk/uniqueness
- appealing to both females and males
- professionalism

I have uploaded our logo in grey or green, I do not mind which one you choose to use (please use either coloured logo on the pure white background not the white on colour version).

Details to include on the business card are:
Names: Corinne Babbage and Pete Oduya
Mobile: 0412 358 214
Email: info@brightwaterdwellings.com.au
Website: www.brightwaterdwellings.com.au (note: this website is currently being developed)
Note: We will provide final details such as mobile number and names on on selection of successful design)

On the other side of the card please include a line similar to "We buy tired, un-renovated properties and sell them looking new again!"

The business card will also need to include the following "ABN 42 139 665 207" which is our Australian Business Number (again the actual number will be provided on selection of successful design). We would like this number somewhere near our name Brightwater Dwellings but in much smaller text.

The purpose of the business cards will be to give to suppliers, real estate agents, people wanting assistance in locating a property in need of renovation and potential buyers.

Thank you and please let me know if you have any further questions.

```html
<!DOCTYPE html>
<html lang="en">
<head>
<meta charset="utf-8">
<title>Brightwater Dwellings – Business Card</title>
<link rel="stylesheet" href="https://fonts.googleapis.com/css2?family=PT+Sans:wght@400;700&family=Libre+Baskerville:wght@700&display=swap">
<style>
  :root {
    --green: #a2c93a;
    --green-deep: #8bbb2e;
    --ink: #231f20;
    --paper: #ffffff;
    --backdrop: #e8e8e6;
    --sans: "PT Sans", sans-serif;
    --serif: "Libre Baskerville", serif;
  }
  * { margin: 0; padding: 0; box-sizing: border-box; }
  html, body {
    width: 1200px;
    height: 857px;
    overflow: hidden;
    background: var(--backdrop);
  }
  .stage { position: relative; width: 1200px; height: 857px; }
  .card {
    position: absolute;
    top: 270px;
    width: 520px;
    height: 318px;
    border-radius: 24px;
    overflow: hidden;
    box-shadow: 0 6px 18px rgba(0,0,0,0.12);
  }
  .card--front { left: 50px; background: var(--paper); }
  .card--back { left: 630px; background: var(--green); }
  .card__shape { position: absolute; inset: 0; }

  .wordmark {
    position: absolute;
    font-family: var(--sans);
    font-weight: 400;
    white-space: nowrap;
    letter-spacing: -0.5px;
  }
  .card--front .wordmark { left: 120px; top: 46px; font-size: 34px; color: var(--green-deep); }
  .card--back .wordmark { right: 38px; top: 118px; font-size: 36px; color: var(--paper); }

  .abn {
    position: absolute;
    font-family: var(--sans);
    font-size: 12px;
    letter-spacing: 0.5px;
    white-space: nowrap;
  }
  .card--front .abn { right: 92px; top: 90px; color: var(--green-deep); }
  .card--back .abn { right: 40px; top: 164px; font-size: 14px; color: var(--paper); }

  .tagline {
    position: absolute;
    right: 40px;
    top: 46px;
    font-family: var(--sans);
    font-size: 12px;
    line-height: 1.35;
    text-align: right;
    color: var(--paper);
  }

  .person { position: absolute; left: 38px; top: 212px; color: var(--ink); white-space: nowrap; }
  .person__name { font-family: var(--serif); font-weight: 700; font-size: 19px; }
  .person__role { font-family: var(--serif); font-weight: 700; font-size: 11px; margin-top: 3px; }

  .contacts {
    position: absolute;
    left: 270px;
    top: 168px;
    list-style: none;
    font-family: var(--sans);
    font-size: 13px;
    color: var(--ink);
    white-space: nowrap;
  }
  .contacts li { display: flex; align-items: center; gap: 7px; height: 20px; }
  .contacts svg { width: 11px; height: 11px; flex: none; }
</style>
</head>
<body>
<main class="stage">

  <section class="card card--front" aria-label="Business card front">
    <svg class="card__shape" viewBox="0 0 520 318" preserveAspectRatio="none" aria-hidden="true">
      <path d="M0,198 C110,168 230,140 330,124 C230,146 110,176 0,214 Z" fill="var(--ink)"/>
      <path d="M0,214 C160,168 340,120 520,98 L520,318 L0,318 Z" fill="var(--green)"/>
    </svg>
    <div class="wordmark">Brightwater Dwellings</div>
    <div class="abn">ABN 42 139 665 207</div>
    <div class="person">
      <div class="person__name">Corinne Babbage</div>
      <div class="person__role">Managing Director</div>
    </div>
    <ul class="contacts">
      <li>
        <svg viewBox="0 0 12 12" aria-hidden="true"><rect x="3" y="0.5" width="6" height="11" rx="1.2" fill="none" stroke="var(--ink)" stroke-width="1.2"/><rect x="5" y="9" width="2" height="1" fill="var(--ink)"/></svg>
        0412 358 214
      </li>
      <li>
        <svg viewBox="0 0 12 12" aria-hidden="true"><rect x="0.5" y="2" width="11" height="8" fill="var(--ink)"/><path d="M0.5,2 L6,6.5 L11.5,2" fill="none" stroke="var(--green)" stroke-width="1"/></svg>
        info@brightwaterdwellings.com.au
      </li>
      <li>
        <svg viewBox="0 0 12 12" aria-hidden="true"><circle cx="6" cy="6" r="5.3" fill="none" stroke="var(--ink)" stroke-width="1.2"/><ellipse cx="6" cy="6" rx="2.2" ry="5.3" fill="none" stroke="var(--ink)" stroke-width="1"/><path d="M0.8,6 H11.2" stroke="var(--ink)" stroke-width="1"/></svg>
        www.brightwaterdwellings.com.au
      </li>
    </ul>
  </section>

  <section class="card card--back" aria-label="Business card back">
    <p class="tagline">We buy tired, un-renovated properties<br>and sell them looking new again!</p>
    <div class="wordmark">Brightwater Dwellings</div>
    <div class="abn">ABN 42 139 665 207</div>
  </section>

</main>
</body>
</html>
```